Business card for partnership

Plumbing and hvac company needing a minimal business card. We already have a logo i would like the front of the card just the logo and the back have all info.

Target Market(s)

Commercial facilities

Industry/Entity Type

Plumbing hvac

Contact Information for Business Card

We would like it double sided. Logo big and bold on the front and out info on the back. Our info on back would be name and position phone, email, and location

```html
<!DOCTYPE html>
<html lang="en">
<head>
<meta charset="utf-8">
<title>Ironvale Mechanical – Business Card</title>
<link rel="stylesheet" href="https://fonts.googleapis.com/css2?family=Oswald:wght@500&family=Arimo:wght@400;700&display=swap">
<style>
  :root {
    --backdrop: #bdbbb6;
    --card: #333333;
    --accent: #f2792b;
    --ink: #ffffff;
    --ink-soft: #e6e6e6;
  }
  html, body {
    margin: 0;
    padding: 0;
    width: 1200px;
    height: 857px;
    overflow: hidden;
    background: var(--backdrop);
  }
  .sheet {
    width: 1200px;
    height: 857px;
    display: flex;
    align-items: center;
    justify-content: center;
    gap: 44px;
  }
  .card {
    position: relative;
    width: 520px;
    height: 297px;
    background: var(--card);
    border-bottom: 3px solid var(--accent);
    border-left: 2px solid var(--accent);
    box-sizing: border-box;
    font-family: "Arimo", Arial, sans-serif;
    color: var(--ink);
  }

  /* Info side */
  .identity {
    position: absolute;
    left: 70px;
    top: 98px;
    text-align: right;
    width: 170px;
  }
  .identity__name {
    font-family: "Oswald", "Arial Narrow", sans-serif;
    font-weight: 500;
    font-size: 27px;
    letter-spacing: 0.5px;
    color: var(--accent);
    text-transform: uppercase;
    line-height: 1.1;
    margin: 0;
  }
  .identity__role {
    font-size: 12px;
    color: var(--ink-soft);
    margin: 3px 0 0;
  }
  .divider {
    position: absolute;
    left: 262px;
    top: 92px;
    width: 1px;
    height: 56px;
    background: var(--ink-soft);
  }
  .contacts {
    position: absolute;
    left: 282px;
    top: 88px;
    margin: 0;
    padding: 0;
    list-style: none;
    font-size: 11px;
    color: var(--ink-soft);
  }
  .contacts li {
    display: flex;
    align-items: center;
    gap: 8px;
    height: 21px;
  }
  .contacts svg {
    width: 10px;
    height: 10px;
    fill: var(--accent);
    flex: none;
  }
  .address {
    position: absolute;
    left: 122px;
    top: 208px;
    font-size: 12px;
    color: var(--ink-soft);
    margin: 0;
  }

  /* Logo side */
  .brand {
    position: absolute;
    inset: 0;
    display: flex;
    align-items: center;
    justify-content: center;
    gap: 12px;
  }
  .brand__mark {
    width: 26px;
    height: 26px;
    background: var(--accent);
  }
  .brand__name {
    font-weight: 700;
    font-size: 34px;
    letter-spacing: 2px;
    text-transform: uppercase;
    color: var(--ink);
    line-height: 1;
    margin: 0;
  }
</style>
</head>
<body>
<main class="sheet">
  <section class="card card--info" aria-label="Card back with contact details">
    <div class="identity">
      <h1 class="identity__name">Daniel Reyes</h1>
      <p class="identity__role">Head of Department</p>
    </div>
    <div class="divider"></div>
    <ul class="contacts">
      <li>
        <svg viewBox="0 0 10 10" aria-hidden="true"><path d="M2 0.5 L3.6 2.6 L2.7 3.6 Q3.8 5.9 6.2 7.2 L7.3 6.3 L9.5 7.9 L8.3 9.5 Q1.6 8.2 0.5 1.7 Z"/></svg>
        <span>+555-204-316</span>
      </li>
      <li>
        <svg viewBox="0 0 10 10" aria-hidden="true"><path d="M0 2 H10 V8.5 H0 Z M0.6 2.4 L5 5.6 L9.4 2.4" stroke="#333" stroke-width="0.8"/></svg>
        <span>reyes.d@ironvalemech.com</span>
      </li>
      <li>
        <svg viewBox="0 0 10 10" aria-hidden="true"><circle cx="5" cy="5" r="4.5"/><path d="M0.5 5 H9.5 M5 0.5 V9.5 M1.5 2.7 H8.5 M1.5 7.3 H8.5" stroke="#333" stroke-width="0.7" fill="none"/></svg>
        <span>www.ironvalemech.com</span>
      </li>
    </ul>
    <p class="address">412 Harbor Road, Coral Point, FL 33021</p>
  </section>

  <section class="card card--brand" aria-label="Card front with company name">
    <div class="brand">
      <span class="brand__mark" aria-hidden="true"></span>
      <p class="brand__name">Ironvale Mechanical</p>
    </div>
  </section>
</main>
</body>
</html>
```